Copper Dunes Website design

Create a sophisticated minimalist shopify ecommerce store that can be integrated with retail express POS.

Copper Dunes is a Brick and mortar store that is focused on exceptional customer service and quality Ladies fashion and specialty swimwear for Women, Men and Children.

This website will need to be easy to navigate by the end user and manage inhouse.

With so many different product categories and customer demographics it will be difficult to make seamless and easy to navigate.

Think The Lumora, Pelko etc where there are Women, Men and Kids

It would be fantastic to build a site with three different navigations to constant themes that are modified to suit each demographic.

We have a logo to use and would like the theme to be easily updated as seasons change and our business evolves.

The website must be set up to use SEO for brixel and other leading search engines.

Stock will be supplied from either our brick and mortar store or warehouse so would need to consist of multiple store locations as far as the back end is concerned.

It will need to be set up with apps that allow us to stream line our fullfilment in house (label printing, picking lists and shipping with Rivo Mail)

```html
<!DOCTYPE html>
<html lang="en">
<head>
<meta charset="utf-8">
<title>Copper Dunes</title>
<link rel="stylesheet" href="https://fonts.googleapis.com/css2?family=Outfit:wght@400;500;600;700;800&family=Poppins:wght@400;500;600;700&display=swap">
<style>
:root{
  --green:#707e5f;
  --ink:#1e1e1e;
  --text:#333;
  --soft:#f3f3f3;
  --tile:#efefef;
  --white:#fff;
  --shade:linear-gradient(180deg,rgba(0,0,0,0) 55%,rgba(0,0,0,.55) 100%);
}
*{box-sizing:border-box;margin:0;padding:0}
html,body{width:1200px;height:4237px;overflow:hidden}
body{position:relative;background:var(--white);font-family:"Poppins",sans-serif;color:var(--text)}
.abs{position:absolute}
.photo{position:absolute;overflow:hidden}
.photo.shaded::after{content:"";position:absolute;inset:0;background:var(--shade)}
.photo .label{position:absolute;z-index:1;left:24px;bottom:18px;color:#fff;font-family:"Outfit",sans-serif;font-weight:700;font-size:30px;letter-spacing:-.5px}

.utility{top:0;left:0;width:1200px;height:26px;display:flex;align-items:center;font-size:8.5px;color:#333}
.utility span{flex:1;text-align:center;border-right:1px solid #bbb;line-height:12px}
.utility span:last-child{border-right:none}

.header{top:26px;left:0;width:1200px;height:79px;background:var(--green)}
.logo{position:absolute;display:flex;align-items:center;gap:7px;font-family:"Outfit",sans-serif;font-weight:500;color:#fff;letter-spacing:2px}
.logo i{display:block;width:9px;height:9px;border-radius:50%;background:#fff}
.header .logo{left:125px;top:29px;font-size:14px}
.mainnav{position:absolute;left:363px;top:33px;display:flex;gap:31px;font-size:9px;font-weight:600;color:#fff;letter-spacing:.3px}
.search{position:absolute;left:718px;top:25px;width:222px;height:31px;background:#fff;border-radius:3px;font-size:8px;color:#999;padding:10px 12px}
.search svg{position:absolute;right:10px;top:9px}
.icons{position:absolute;left:984px;top:28px;display:flex;gap:16px}

.catbar{top:105px;left:125px;width:950px;height:45px;display:flex;align-items:center;font-size:9px;color:#333}
.catbar span{flex:1;text-align:center;border-right:1px solid #bbb;line-height:12px}
.catbar span:last-child{border-right:none}

.hero{top:150px;left:0;width:1200px;height:534px;background:var(--soft)}
.hero h2{position:absolute;left:123px;top:144px;font-family:"Outfit",sans-serif;font-weight:600;font-size:39px;color:var(--ink);letter-spacing:-1px}
.hero h1{position:absolute;left:119px;top:183px;font-family:"Outfit",sans-serif;font-weight:700;font-size:98px;color:var(--ink);letter-spacing:-3px;line-height:1.1}
.hero p{position:absolute;left:125px;top:298px;width:350px;font-size:11px;line-height:17px;color:#444}
.btn{position:absolute;background:var(--green);color:#fff;font-size:8px;font-weight:600;display:flex;align-items:center;justify-content:center;border-radius:2px;letter-spacing:.2px}

.title{position:absolute;left:125px;font-family:"Outfit",sans-serif;font-weight:600;font-size:21px;color:var(--ink);letter-spacing:-.5px}
.arrows{position:absolute;left:1024px;display:flex;gap:5px}
.arrows b{width:22px;height:22px;display:flex;align-items:center;justify-content:center;font-size:11px;font-weight:500;background:#e2e2e2;color:#555}
.arrows b+b{background:var(--green);color:#fff}

.band{top:1407px;left:0;width:1200px;height:755px;background:var(--soft)}
.season h2{position:absolute;left:695px;font-family:"Outfit",sans-serif;font-weight:600;font-size:56px;letter-spacing:-1.5px;line-height:1}
.row{position:absolute;left:125px;width:950px;display:flex;gap:10px}
.row .photo{position:relative}
.caption{position:absolute;font-size:11px;font-weight:600;color:var(--ink);text-align:center}

.cta{position:absolute;height:53px;width:470px;display:flex;align-items:center;justify-content:center;color:#fff;font-size:10px;font-weight:600;letter-spacing:.2px}
.cta svg{position:absolute;right:26px}

.brand{width:150px;height:137px;background:var(--tile);display:flex;align-items:center;justify-content:center;font-family:"Outfit",sans-serif;font-weight:700;font-size:17px;color:#222;text-align:center;line-height:1.1}

.footer{top:3673px;left:0;width:1200px;height:564px;background:var(--green);color:#fff}
.footer h4{position:absolute;font-size:8.5px;font-weight:600;letter-spacing:.2px}
.flist{position:absolute;font-size:7.8px;line-height:13.7px;list-style:none;color:#f2f2f2}
.footer .rule{position:absolute;left:125px;top:158px;width:950px;height:1px;background:rgba(255,255,255,.3)}
.social li{display:flex;align-items:center;gap:6px;line-height:15px}
.social li i{display:block;width:6px;height:6px;border-radius:50%;background:#fff}
.signup{position:absolute;left:768px;top:246px;width:307px;height:30px;display:flex;gap:3px}
.signup div{background:#fff;color:#666;font-size:7.5px;display:flex;align-items:center;padding:0 10px}
.badge{position:absolute;top:471px;width:120px;height:36px;background:#fff;border-radius:4px;color:#111;display:flex;align-items:center;gap:7px;padding:0 11px}
.badge i{display:block;width:11px;height:11px;background:#222;border-radius:2px}
.badge small{display:block;font-size:5.5px}
.badge strong{display:block;font-size:10px;font-weight:600;line-height:1}
.chat{position:absolute;left:1104px;top:4060px;width:66px;height:66px;border-radius:50%;background:#ebebeb;display:flex;align-items:center;justify-content:center;box-shadow:0 2px 8px rgba(0,0,0,.15)}
</style>
</head>
<body>

<div class="abs utility">
  <span>Contact &amp; FAQs</span><span>Delivery</span><span>Returns</span><span>Track Orders</span><span>Share Your Ideas</span><span>Gift Cards</span>
</div>

<header class="abs header">
  <div class="logo"><i></i>COPPER DUNES</div>
  <nav class="mainnav"><span>HOME</span><span>WOMEN</span><span>MEN</span><span>KIDS</span><span>SHORT</span><span>BEAUTY</span></nav>
  <div class="search">Search for products, brands...
    <svg width="12" height="12" viewBox="0 0 12 12" fill="none" stroke="#333" stroke-width="1.4"><circle cx="5" cy="5" r="3.8"/><path d="M8 8l3 3"/></svg>
  </div>
  <div class="icons">
    <svg width="20" height="20" viewBox="0 0 20 20" fill="none" stroke="#fff" stroke-width="1.4"><circle cx="10" cy="6.5" r="4"/><path d="M3 18c1-4 4-6 7-6s6 2 7 6"/></svg>
    <svg width="22" height="20" viewBox="0 0 22 20" fill="none" stroke="#fff" stroke-width="1.4"><path d="M11 18S2 12 2 6.5A4.5 4.5 0 0 1 11 4a4.5 4.5 0 0 1 9 2.5C20 12 11 18 11 18z"/></svg>
    <svg width="20" height="20" viewBox="0 0 20 20" fill="none" stroke="#fff" stroke-width="1.4"><path d="M1 3h3l2.5 10h10L19 6H5.5"/><circle cx="8" cy="17" r="1.3"/><circle cx="15" cy="17" r="1.3"/></svg>
  </div>
</header>

<nav class="abs catbar">
  <span>NEW IN</span><span>CLOTHING</span><span>SHOES</span><span>ACCESSORIES</span><span>SPORT</span><span>BRANDS</span><span>DESIGNER</span><span>SNEAKERHUB</span>
</nav>

<section class="abs hero">
  <h2>Effortless Elegance,</h2>
  <h1>Everyday.</h1>
  <p>Discover timeless styles and statement swimwear designed to flatter every season.</p>
  <div class="btn" style="left:125px;top:351px;width:153px;height:34px">SHOP THE COLLECTION</div>
  <div class="photo" role="img" aria-label="Three smiling women in sunglasses and denim jackets" style="left:559px;top:0;width:641px;height:534px;background:
    radial-gradient(ellipse 90px 260px at 22% 62%,rgba(72,112,140,.85),transparent 70%),
    radial-gradient(ellipse 130px 280px at 50% 58%,rgba(38,92,112,.9),transparent 70%),
    radial-gradient(ellipse 80px 140px at 22% 88%,rgba(214,148,60,.85),transparent 70%),
    radial-gradient(ellipse 120px 230px at 86% 60%,rgba(222,196,176,.9),transparent 72%),
    radial-gradient(ellipse 70px 60px at 28% 14%,rgba(212,170,140,.9),transparent 70%),
    radial-gradient(ellipse 80px 70px at 50% 20%,rgba(150,98,64,.85),transparent 70%),
    radial-gradient(ellipse 80px 70px at 86% 18%,rgba(196,140,96,.85),transparent 70%),
    #f1f0ee"></div>
</section>

<div class="photo shaded" role="img" aria-label="Two women in patterned outfits on city steps" style="left:125px;top:787px;width:301px;height:227px;background:
  radial-gradient(ellipse 60px 100px at 38% 55%,rgba(40,72,60,.9),transparent 70%),
  radial-gradient(ellipse 60px 90px at 60% 58%,rgba(236,236,232,.8),transparent 70%),
  linear-gradient(180deg,#a9a8a4 0%,#7d7f78 50%,#55574f 100%)"><span class="label">Women’s</span></div>
<div class="photo shaded" role="img" aria-label="Group of children against striped wall" style="left:439px;top:787px;width:301px;height:227px;background:
  radial-gradient(ellipse 110px 80px at 55% 60%,rgba(150,48,52,.7),transparent 70%),
  repeating-linear-gradient(90deg,#1f1f1f 0 18px,#e8e8e8 18px 36px)"><span class="label">Kid’s</span></div>
<div class="photo shaded" role="img" aria-label="Woman in printed swimsuit on the beach" style="left:125px;top:1027px;width:615px;height:226px;background:
  radial-gradient(ellipse 120px 70px at 70% 55%,rgba(110,66,44,.8),transparent 70%),
  radial-gradient(ellipse 300px 40px at 70% 20%,rgba(170,190,196,.7),transparent 70%),
  linear-gradient(180deg,#d4c6b4 0%,#c2ae96 60%,#9b8670 100%)"><span class="label">Swimwear</span></div>
<div class="photo shaded" role="img" aria-label="Bearded man in black graphic t-shirt" style="left:753px;top:787px;width:322px;height:466px;background:
  radial-gradient(ellipse 60px 80px at 50% 22%,rgba(150,112,96,.9),transparent 70%),
  radial-gradient(ellipse 150px 200px at 50% 68%,rgba(18,18,20,.95),transparent 72%),
  linear-gradient(180deg,#a9adb1 0%,#8a8d90 50%,#5c5e61 100%)"><span class="label">Men’s</span></div>

<div class="abs band"></div>
<div class="photo" role="img" aria-label="Three women in sunglasses and blouses against a stone wall" style="left:125px;top:1355px;width:511px;height:450px;background:
  radial-gradient(ellipse 70px 140px at 24% 45%,rgba(250,250,248,.95),transparent 70%),
  radial-gradient(ellipse 70px 140px at 48% 48%,rgba(236,190,190,.95),transparent 70%),
  radial-gradient(ellipse 85px 150px at 76% 46%,rgba(28,28,30,.95),transparent 70%),
  radial-gradient(ellipse 230px 70px at 50% 88%,rgba(120,136,160,.85),transparent 72%),
  radial-gradient(ellipse 50px 50px at 24% 15%,rgba(190,150,110,.9),transparent 70%),
  radial-gradient(ellipse 50px 50px at 50% 16%,rgba(220,200,160,.9),transparent 70%),
  radial-gradient(ellipse 55px 55px at 78% 15%,rgba(40,30,28,.9),transparent 70%),
  #d6d4d0"></div>
<div class="season">
  <h2 style="top:1452px;color:var(--ink)">New Season.</h2>
  <h2 style="top:1508px;color:var(--green)">New Styles</h2>
</div>
<p class="abs" style="left:697px;top:1582px;font-size:13px;font-weight:500;color:var(--ink)">Update your wardrobe with our latest arrivals.</p>
<div class="btn" style="left:699px;top:1627px;width:151px;height:35px">SHOP THE COLLECTION</div>

<h3 class="title" style="top:1889px">Shop Your Favourites</h3>
<div class="arrows" style="top:1893px"><b>‹</b><b>›</b></div>
<div class="row" style="top:1937px">
  <div class="photo" role="img" aria-label="Woman in pink floral jacket" style="width:150px;height:167px;background:radial-gradient(ellipse 55px 75px at 50% 55%,#d9978a,transparent 72%),#f5f1ee"></div>
  <div class="photo" role="img" aria-label="Woman in black leather jacket" style="width:150px;height:167px;background:radial-gradient(ellipse 60px 80px at 50% 62%,#242221,transparent 72%),#d8cdc1"></div>
  <div class="photo" role="img" aria-label="Woman in grey knit sweater" style="width:150px;height:167px;background:radial-gradient(ellipse 55px 80px at 50% 62%,#7e7e7d,transparent 72%),#d2d1ce"></div>
  <div class="photo" role="img" aria-label="Woman in denim shorts and blue top" style="width:150px;height:167px;background:radial-gradient(ellipse 40px 50px at 50% 45%,#9fc5e0,transparent 72%),radial-gradient(ellipse 45px 30px at 50% 82%,#4c6c9c,transparent 72%),#f4f4f4"></div>
  <div class="photo" role="img" aria-label="Feet in beige flat shoes and jeans" style="width:150px;height:167px;background:radial-gradient(ellipse 70px 60px at 50% 35%,#b5c3d6,transparent 72%),radial-gradient(ellipse 55px 25px at 50% 78%,#d8c09e,transparent 72%),#ece9e6"></div>
  <div class="photo" role="img" aria-label="Woman in grey sports bra and leggings" style="width:150px;height:167px;background:radial-gradient(ellipse 30px 25px at 50% 42%,#c9c6c8,transparent 72%),radial-gradient(ellipse 40px 50px at 50% 80%,#1f1e22,transparent 72%),#bdbcc3"></div>
</div>
<div class="caption" style="left:125px;top:2118px;width:150px">Dresses</div>
<div class="caption" style="left:285px;top:2118px;width:150px">Coats &amp; Jackets</div>
<div class="caption" style="left:445px;top:2118px;width:150px">Knitwear</div>
<div class="caption" style="left:605px;top:2118px;width:150px">Jeans</div>
<div class="caption" style="left:765px;top:2118px;width:150px">Flats</div>
<div class="caption" style="left:925px;top:2118px;width:150px">Activewear</div>

<h3 class="title" style="top:2257px">Shop The Latest</h3>
<div class="arrows" style="top:2261px"><b>‹</b><b>›</b></div>
<div class="photo shaded" role="img" aria-label="Woman in checked dress and sunglasses on a city street" style="left:125px;top:2310px;width:469px;height:452px;background:
  radial-gradient(ellipse 90px 190px at 42% 55%,rgba(226,224,220,.95),transparent 70%),
  radial-gradient(ellipse 140px 110px at 22% 10%,rgba(150,96,70,.85),transparent 70%),
  repeating-linear-gradient(90deg,#8e8b86 0 26px,#b6b3ae 26px 40px),
  #777"><span class="label" style="left:31px;bottom:26px;font-size:31px">Desire: VELLA SS25</span></div>
<div class="photo shaded" role="img" aria-label="Woman in red knit set crouching" style="left:605px;top:2310px;width:470px;height:222px;background:radial-gradient(ellipse 70px 75px at 68% 48%,rgba(176,36,40,.95),transparent 72%),#f0efee"><span class="label" style="left:26px;font-size:24px">Spring into Motion</span></div>
<div class="photo shaded" role="img" aria-label="Skincare bottles on stone plinths with dried flowers" style="left:605px;top:2540px;width:470px;height:222px;background:
  radial-gradient(ellipse 90px 55px at 64% 72%,rgba(244,240,234,.95),transparent 72%),
  radial-gradient(ellipse 30px 50px at 74% 40%,rgba(250,248,244,.95),transparent 72%),
  linear-gradient(180deg,#e2d8cd,#cdbfb0)"><span class="label" style="left:26px;font-size:24px">Spring Renewal</span></div>
<div class="cta" style="left:125px;top:2780px;background:var(--green)">NEW HERE? $20 OFF YOUR FIRST PURCHASE
  <svg width="16" height="10" viewBox="0 0 16 10" fill="none" stroke="#fff" stroke-width="1.2"><path d="M0 5h15M11 1l4 4-4 4"/></svg></div>
<div class="cta" style="left:605px;top:2780px;background:#1f1f1f">GET $20 CREDIT WHEN YOU REFER A FRIEND
  <svg width="16" height="10" viewBox="0 0 16 10" fill="none" stroke="#fff" stroke-width="1.2"><path d="M0 5h15M11 1l4 4-4 4"/></svg></div>

<h3 class="title" style="top:2950px">Shop by Category</h3>
<div class="arrows" style="top:2954px"><b>‹</b><b>›</b></div>
<div class="row" style="top:2995px">
  <div class="photo" role="img" aria-label="Two people stretching in sportswear against a mural" style="width:230px;height:227px;background:radial-gradient(ellipse 50px 90px at 30% 60%,#ececea,transparent 72%),radial-gradient(ellipse 55px 80px at 72% 62%,#24262a,transparent 72%),linear-gradient(135deg,#8fb0bd,#d7d2c9 55%,#a6b8c0)"></div>
  <div class="photo" role="img" aria-label="Woman with hair rollers applying beauty products" style="width:230px;height:227px;background:radial-gradient(ellipse 65px 80px at 50% 50%,#b08a74,transparent 72%),radial-gradient(ellipse 70px 60px at 50% 88%,#c8c2ba,transparent 72%),#c4a9cc"></div>
  <div class="photo" role="img" aria-label="Woman in yellow dress with red handbag on a lounge chair" style="width:230px;height:227px;background:radial-gradient(ellipse 40px 60px at 45% 45%,#e8dc3e,transparent 72%),radial-gradient(ellipse 30px 25px at 28% 78%,#c8302a,transparent 72%),radial-gradient(ellipse 60px 25px at 55% 85%,#5b8a4a,transparent 72%),#d5cdc1"></div>
  <div class="photo" role="img" aria-label="Man in glasses writing at a desk" style="width:230px;height:227px;background:radial-gradient(ellipse 70px 70px at 52% 55%,#8ea6c8,transparent 72%),radial-gradient(ellipse 60px 70px at 90% 15%,#b33a33,transparent 72%),radial-gradient(ellipse 40px 100px at 8% 40%,#8a7a5c,transparent 72%),#e6e2dc"></div>
</div>
<div class="caption" style="left:125px;top:3236px;width:230px">Sport</div>
<div class="caption" style="left:365px;top:3236px;width:230px">Beauty</div>
<div class="caption" style="left:605px;top:3236px;width:230px">Women’s Designer</div>
<div class="caption" style="left:845px;top:3236px;width:230px">Men’s Designer</div>

<h3 class="title" style="top:3386px">Shop brands</h3>
<div class="arrows" style="top:3390px"><b>‹</b><b>›</b></div>
<div class="row" style="top:3434px">
  <div class="brand">Vantor</div>
  <div class="brand">Colt &amp;<br>Marlowe</div>
  <div class="brand">Ridgeway</div>
  <div class="brand">Maison Verel</div>
  <div class="brand">Strivo</div>
  <div class="brand">Odette &amp; Lune</div>
</div>

<footer class="abs footer">
  <h4 style="left:125px;top:46px">OUR TOP SEARCHES</h4>
  <ul class="flist" style="left:125px;top:72px"><li>Ridgeway</li><li>Vantor</li><li>Makeup</li><li>Ned Barlow</li></ul>
  <ul class="flist" style="left:252px;top:72px"><li>Solestead</li><li>Amarin</li><li>Coastline Lane</li><li>Shoes</li></ul>
  <ul class="flist" style="left:383px;top:72px"><li>Kickline</li><li>Sagewell</li><li>Dekk</li><li>Always Bloom</li></ul>
  <ul class="flist" style="left:516px;top:72px"><li>Willowmere</li><li>Skincare</li><li>Packmont</li><li>Marivel</li></ul>
  <ul class="flist" style="left:636px;top:72px"><li>Tessa Fay</li><li>True Stride</li><li>Strivo</li><li>Swimwear</li></ul>
  <ul class="flist" style="left:753px;top:72px"><li>Corin Vale</li><li>Sunvale</li><li>Lynxa</li><li>Colt &amp; Marlowe</li></ul>
  <ul class="flist" style="left:899px;top:72px"><li>Sneakers</li><li>Sandals</li><li>Kaido</li><li>Dresses</li></ul>
  <ul class="flist" style="left:1014px;top:72px"><li>Jeans</li><li>Theo Harwick</li><li>Rocco Blanc</li><li>Form Nation</li></ul>
  <div class="rule"></div>

  <h4 style="left:125px;top:197px">COPPER DUNES</h4>
  <ul class="flist" style="left:125px;top:221px"><li>About Us</li><li>Acknowledgement Of Country</li><li>Affiliates</li><li>Brands</li><li>Partnerships</li><li>Influencers</li><li>Press</li><li>Careers</li><li>Terms &amp; Conditions</li><li>Promotions and Competitions</li><li>Privacy Policy</li><li>Online Security Advice</li></ul>
  <h4 style="left:375px;top:197px">HELP &amp; SUPPORT</h4>
  <ul class="flist" style="left:375px;top:221px"><li>FAQs &amp; Contact</li><li>Delivery</li><li>Returns</li><li>Size Guide</li><li>Gift Cards</li><li>Fashion Glossary</li><li>Product Ideas</li><li>Product Recall</li></ul>
  <h4 style="left:587px;top:197px">FOLLOW US</h4>
  <ul class="flist social" style="left:587px;top:221px"><li><i></i>Snapgrid</li><li><i></i>Friendloop</li><li><i></i>Chirpa</li><li><i></i>Pinboardly</li><li><i></i>Vidstream</li></ul>
  <h4 style="left:768px;top:197px">STAY IN TOUCH</h4>
  <p class="abs" style="left:768px;top:221px;font-size:7.8px">Sign up to COPPER DUNES News for your <b>$20 voucher.</b>*</p>
  <div class="signup">
    <div style="width:74px;justify-content:space-between;color:#222">Women <span>⌄</span></div>
    <div style="flex:1">Enter your email address</div>
    <div style="width:72px;justify-content:center;color:#222;font-weight:600">SUBMIT</div>
  </div>

  <p class="abs" style="left:125px;top:483px;font-size:8px">© COPYRIGHT 2025 COPPER DUNES ALL RIGHTS RESERVED</p>
  <div class="logo" style="left:518px;top:480px;font-size:16px"><i></i>COPPER DUNES</div>
  <div class="badge" style="left:825px"><i></i><div><small>GET IT ON</small><strong>Orchard Store</strong></div></div>
  <div class="badge" style="left:953px"><i></i><div><small>DOWNLOAD ON THE</small><strong>Brixel Play</strong></div></div>
</footer>

<div class="chat">
  <svg width="30" height="28" viewBox="0 0 30 28" fill="none"><path d="M15 2C7.8 2 2 6.7 2 12.5c0 3.3 1.9 6.2 4.8 8.1L5.5 26l6.2-3.2c1.1.2 2.2.3 3.3.3 7.2 0 13-4.7 13-10.6S22.2 2 15 2z" fill="#fff" stroke="#666" stroke-width="1.6"/><circle cx="10" cy="12.5" r="1.6" fill="#666"/><circle cx="15" cy="12.5" r="1.6" fill="#666"/><circle cx="20" cy="12.5" r="1.6" fill="#666"/></svg>
</div>

</body>
</html>
```